THE 4 (THREE-SIDED) PYRAMIDS OF "THE 9 LANTERNS"

I WOULD LIKE TO CREATE DESIGN FOR MY 4 "TRILATERAL" (THREE-SIDED) PYRAMIDS WHICH MAKE UP THE 9 LANTERNS. IN ADDITION I WOULD LIKE TO SEE DESIGNS WITH THE PYRAMIDS OVERLAPPING AT 30 DEGREES. THESE DESIGNS NEED TO BE ABLE TO COPY AND PASTED ON MULTIPLE DIFFERENT APPLICATIONS

Font styles to use
Sans Serif

Colors
6b439a
00a990
ec1f27
3277b5

Requirements
Must have
• EACH PYRAMID HAS A DESIGNATED COLOR. THE 1ST PYRAMID IS PURPLE- THE HIGHEST LEVEL SHOULD BE DARK PURPLE AND THE LOWER LEVELS DECRESING SHADES OF PURPLE. THIS SHOULD BE REPEATED FOR THE GREEEN, RED AND BLUE PYRAMIDS. EACH CORNER OF EVERY LEVEL SHOULD HAVE THE WORD OR WORDS AFFILIATED TO THAT CONNER LABELLED

```html
<!DOCTYPE html>
<html lang="en">
<head>
<meta charset="utf-8">
<title>Pyramid of Realms</title>
<link rel="stylesheet" href="https://fonts.googleapis.com/css2?family=Rubik:wght@500&display=swap">
<style>
  :root {
    --bg: #ffffff;
    --label: #7b2590;
    --label-soft: #c06cb0;
    --inner: #ffffff;
    --tier-0: #7d2490;
    --tier-1: #8a3895;
    --tier-2: #9b4f9e;
    --tier-3: #b168a9;
    --tier-4: #c385b9;
    --tier-5: #d6a4ca;
    --tier-6: #ecc8de;
    --seam: rgba(255,255,255,0.45);
  }
  html, body { margin: 0; padding: 0; overflow: hidden; background: var(--bg); }
  .canvas { width: 1200px; height: 1200px; display: block; }
  .pyramid text { font-family: "Rubik", sans-serif; font-weight: 500; }
  .corner-label { fill: var(--label); font-size: 20px; }
  .tier-label { fill: var(--inner); font-size: 20px; text-anchor: middle; }
  .base-label { fill: var(--label-soft); font-size: 20px; text-anchor: middle; }
  .label-left { text-anchor: end; }
  .label-right { text-anchor: start; }
  .tier-0 { fill: var(--tier-0); } .tier-1 { fill: var(--tier-1); }
  .tier-2 { fill: var(--tier-2); } .tier-3 { fill: var(--tier-3); }
  .tier-4 { fill: var(--tier-4); } .tier-5 { fill: var(--tier-5); }
  .tier-6 { fill: var(--tier-6); }
  .seam { stroke: var(--seam); stroke-width: 3; fill: none; }
  .level-line { stroke: rgba(255,255,255,0.2); stroke-width: 2; }
  .face-sheen { fill: url(#sheen); }
</style>
</head>
<body>
<svg class="canvas pyramid" viewBox="0 0 1380 1380" xmlns="http://www.w3.org/2000/svg">
  <defs>
    <linearGradient id="sheen" x1="0" y1="0" x2="1" y2="0">
      <stop offset="0" stop-color="#fff" stop-opacity="0"/>
      <stop offset="1" stop-color="#fff" stop-opacity="0.22"/>
    </linearGradient>
  </defs>

  <g class="left-face">
    <polygon class="tier-0" points="668,172 610,285 668,305"/>
    <polygon class="tier-1" points="610,285 668,305 668,435 543,402"/>
    <polygon class="tier-2" points="543,402 668,435 668,565 482,515"/>
    <polygon class="tier-3" points="482,515 668,565 668,697 420,628"/>
    <polygon class="tier-4" points="420,628 668,697 668,828 358,742"/>
    <polygon class="tier-5" points="358,742 668,828 668,958 298,855"/>
    <polygon class="tier-6" points="298,855 668,958 668,1090 236,968"/>
    <polygon class="face-sheen" points="668,172 236,968 668,1090"/>
  </g>
  <g class="right-face">
    <polygon class="tier-0" points="668,172 727,285 668,305"/>
    <polygon class="tier-1" points="727,285 668,305 668,435 790,402"/>
    <polygon class="tier-2" points="790,402 668,435 668,565 852,515"/>
    <polygon class="tier-3" points="852,515 668,565 668,697 914,628"/>
    <polygon class="tier-4" points="914,628 668,697 668,828 976,742"/>
    <polygon class="tier-5" points="976,742 668,828 668,958 1038,855"/>
    <polygon class="tier-6" points="1038,855 668,958 668,1090 1100,968"/>
  </g>

  <g class="level-lines">
    <line class="level-line" x1="543" y1="402" x2="790" y2="402"/>
    <line class="level-line" x1="482" y1="515" x2="852" y2="515"/>
    <line class="level-line" x1="420" y1="628" x2="914" y2="628"/>
    <line class="level-line" x1="358" y1="742" x2="976" y2="742"/>
    <line class="level-line" x1="298" y1="855" x2="1038" y2="855"/>
    <line class="level-line" x1="236" y1="968" x2="1100" y2="968"/>
  </g>
  <g class="seams">
    <polyline class="seam" points="610,285 668,305 727,285"/>
    <polyline class="seam" points="543,402 668,435 790,402"/>
    <polyline class="seam" points="482,515 668,565 852,515"/>
    <polyline class="seam" points="420,628 668,697 914,628"/>
    <polyline class="seam" points="358,742 668,828 976,742"/>
    <polyline class="seam" points="298,855 668,958 1038,855"/>
    <polyline class="seam" points="236,968 668,1090 1100,968"/>
  </g>

  <g class="tier-labels">
    <text class="tier-label" x="668" y="329">God</text>
    <text class="tier-label" x="668" y="354">the Father</text>
    <text class="tier-label" x="668" y="456">Love</text>
    <text class="tier-label" x="668" y="592">Ask- Believe</text>
    <text class="tier-label" x="668" y="722">Mind</text>
    <text class="tier-label" x="668" y="855">Self-Condemnation</text>
    <text class="tier-label" x="668" y="882">(Self Hate)</text>
    <text class="tier-label" x="668" y="986">Unforgiveness</text>
    <text class="tier-label" x="668" y="1010">(Hate/ Hatred of Others)</text>
  </g>

  <g class="corner-labels">
    <text class="corner-label label-left" x="592" y="296">God the Son</text>
    <text class="corner-label label-left" x="537" y="410">Peace</text>
    <text class="corner-label label-left" x="474" y="523">Seek- Obedience</text>
    <text class="corner-label label-left" x="412" y="636">Body</text>
    <text class="corner-label label-left" x="349" y="749">Fear</text>
    <text class="corner-label label-left" x="289" y="863">Anger</text>
    <text class="corner-label label-left" x="228" y="968">External Disease</text>
    <text class="corner-label label-left" x="228" y="993">(Leprosy)</text>

    <text class="corner-label label-right" x="737" y="296">God the Holy Spirit</text>
    <text class="corner-label label-right" x="802" y="410">Joy</text>
    <text class="corner-label label-right" x="863" y="523">Knock- Receive</text>
    <text class="corner-label label-right" x="924" y="636">Soul</text>
    <text class="corner-label label-right" x="988" y="749">Worry</text>
    <text class="corner-label label-right" x="1048" y="863">Doubt</text>
    <text class="corner-label label-right" x="1108" y="965">Mental and</text>
    <text class="corner-label label-right" x="1108" y="990">Psychological Disease</text>
    <text class="corner-label label-right" x="1108" y="1015">(Fits and Seizures/</text>
    <text class="corner-label label-right" x="1108" y="1040">“demon-possessed”)</text>

    <text class="base-label" x="668" y="1115">Internal Disease</text>
    <text class="base-label" x="668" y="1143">(The issue of blood)</text>
  </g>
</svg>
</body>
</html>
```